Business Card Design Project

I want a cleaner business card and envelope then what we have now, its too crowded.
Updates

I update with logo, this can be changed anyway you feel it looks best. I also have put gaurantee on there and extended time, this is my first time doing this. Also gave an example of current card

Target Market(s)

a wide array of customers from lattice 700 to small companies and cleints

Industry/Entity Type

Business

Requirements
Must have
• Need to have address, telephone number email
Nice to have
• a sharp professional card that stands out but is still very clean.
Should not have
• Not crazy looking

```html
<!DOCTYPE html>
<html lang="en">
<head>
<meta charset="utf-8">
<title>Calloway Insurance Group – Business Card</title>
<link rel="stylesheet" href="https://fonts.googleapis.com/css2?family=Questrial&family=Montserrat:wght@600&display=swap">
<style>
  :root {
    --backdrop: #dfe3e5;
    --silver-light: #f4f4f4;
    --silver-mid: #c9c9c9;
    --silver-dark: #8e8e8e;
    --paper: #ffffff;
    --ink: #2f2f2f;
    --ink-soft: #4a4a4a;
    --tab: #5a5a5a;
    --card-shadow: rgba(0, 0, 0, 0.18);
  }
  html, body {
    margin: 0;
    padding: 0;
    width: 1200px;
    height: 960px;
    overflow: hidden;
    background: var(--backdrop);
    font-family: "Questrial", "Century Gothic", sans-serif;
  }
  .canvas {
    position: relative;
    width: 1200px;
    height: 960px;
  }
  .card {
    position: absolute;
    left: 250px;
    width: 700px;
    height: 400px;
    box-shadow: 0 10px 28px var(--card-shadow);
    overflow: hidden;
  }
  .card-front {
    top: 60px;
    background: linear-gradient(115deg, var(--silver-dark) 0%, var(--silver-mid) 30%, var(--silver-light) 52%, var(--silver-mid) 70%, var(--silver-dark) 100%);
    display: flex;
    flex-direction: column;
    align-items: center;
    justify-content: center;
  }
  .card-back {
    top: 500px;
    background: var(--paper);
  }
  .brand {
    display: flex;
    flex-direction: column;
    align-items: center;
    color: var(--ink);
    font-weight: 400;
  }
  .brand-square {
    width: 70px;
    height: 70px;
    background: var(--ink-soft);
    margin-bottom: 22px;
  }
  .brand-name {
    font-size: 44px;
    letter-spacing: 3px;
    line-height: 1;
  }
  .brand-sub {
    font-size: 19px;
    letter-spacing: 2.5px;
    margin-top: 6px;
  }
  .card-back .brand {
    position: absolute;
    left: 40px;
    top: 118px;
    width: 250px;
  }
  .card-back .brand-square {
    width: 48px;
    height: 48px;
    margin-bottom: 14px;
  }
  .card-back .brand-name { font-size: 28px; letter-spacing: 2px; }
  .card-back .brand-sub { font-size: 12px; letter-spacing: 1.8px; margin-top: 4px; }
  .contact {
    position: absolute;
    left: 345px;
    top: 58px;
    color: var(--ink);
  }
  .person-name { font-size: 25px; letter-spacing: 0.5px; }
  .person-title { font-size: 20px; margin-top: 2px; }
  .details {
    list-style: none;
    margin: 36px 0 0;
    padding: 0;
    font-size: 16px;
    line-height: 20px;
  }
  .details li {
    display: flex;
    align-items: flex-start;
  }
  .details svg {
    width: 11px;
    height: 11px;
    margin: 4px 7px 0 0;
    flex: none;
    fill: var(--ink-soft);
  }
  .details .indent { padding-left: 18px; }
  .website {
    font-family: "Montserrat", sans-serif;
    font-weight: 600;
    font-size: 15px;
    margin-top: 24px;
    letter-spacing: 0.3px;
  }
  .edge-tab {
    position: absolute;
    right: 0;
    top: 70px;
    width: 38px;
    height: 46px;
    background: var(--tab);
    clip-path: polygon(22% 0, 100% 0, 100% 100%, 22% 100%, 0 50%);
  }
</style>
</head>
<body>
<main class="canvas">
  <section class="card card-front" aria-label="Card front">
    <div class="brand">
      <div class="brand-square"></div>
      <div class="brand-name">CALLOWAY</div>
      <div class="brand-sub">INSURANCE GROUP</div>
    </div>
  </section>

  <section class="card card-back" aria-label="Card back">
    <div class="brand">
      <div class="brand-square"></div>
      <div class="brand-name">CALLOWAY</div>
      <div class="brand-sub">INSURANCE GROUP</div>
    </div>
    <div class="contact">
      <div class="person-name">Marla Quinn-Everett</div>
      <div class="person-title">Operations manager</div>
      <ul class="details">
        <li><svg viewBox="0 0 12 12"><path d="M3 1l2 2.5-1.2 1.2c.6 1.3 1.6 2.3 2.9 2.9L7.9 6.4 10.5 8.4 9.4 10.6C5.2 10.4 1.6 6.8 1.4 2.6z"/></svg>555-214-3800 ext 118</li>
        <li><svg viewBox="0 0 12 12"><path d="M1 2.5h10v7H1z M1.6 3l4.4 3.4L10.4 3z" fill-rule="evenodd"/></svg>mquinn-everett@callowayagency.com</li>
        <li><svg viewBox="0 0 12 12"><circle cx="6" cy="6" r="5"/></svg>1870 Alder Crest Ave.</li>
        <li class="indent">Brookfield Hills, MI 48000</li>
      </ul>
      <div class="website">www.callowayagency.com</div>
    </div>
    <div class="edge-tab"></div>
  </section>
</main>
</body>
</html>
```